Mexican construction company needs a business card design

We need a business card design for a company based in Monterrey, Mexico called:

Desarrollos Tolvani S.A. de C.V.

The company is in the construction business and I would like the businees card to be simple and concise. Please use white background and blue or black text color that say:

"Proyectos de Construcción"-- (Brief description of business)
" Rodrigo Ulloa Benítez"--- (My name)
"rulloab@correovelo.mx"-- (My email)
"C: (81) 82 19 57 46"-- (My cell)
"O: (81) 86 72 13 95"-- (Office phone)

Please use only the colors of my company that are attached

Please make the back of the business card blue (same blue from logo) and use the logo.

Thanks!

```html
<!DOCTYPE html>
<html lang="es">
<head>
<meta charset="utf-8">
<title>Desarrollos Tolvani – Tarjeta de presentación</title>
<link rel="stylesheet" href="https://fonts.googleapis.com/css2?family=Saira:wght@400;600;700&display=swap">
<style>
  :root {
    --navy: #06003c;
    --paper: #f6f6f6;
    --rule: #8a8a96;
    --ink-soft: #5c5c66;
    --backdrop: #575757;
    --white: #ffffff;
  }
  * { margin: 0; padding: 0; box-sizing: border-box; }
  html, body {
    width: 1200px; height: 750px; overflow: hidden;
    background: var(--backdrop);
    font-family: "Saira", sans-serif;
  }
  .canvas { position: relative; width: 1200px; height: 750px; }

  .card {
    position: absolute;
    left: 371px;
    width: 462px;
    height: 263px;
    overflow: hidden;
  }

  /* Front */
  .card--front { top: 129px; background: var(--paper); }
  .brand {
    position: absolute; top: 56px; left: 0; right: 0;
    display: flex; justify-content: center; align-items: center; gap: 12px;
  }
  .brand__square { width: 40px; height: 40px; background: var(--navy); }
  .brand__name {
    color: var(--navy); font-weight: 700; line-height: 1;
    text-transform: uppercase;
  }
  .brand__line1 { display: block; font-size: 14px; letter-spacing: 1.6px; margin-bottom: 3px; }
  .brand__line2 { display: block; font-size: 28px; letter-spacing: 0.5px; }

  .contact {
    position: absolute; top: 160px; left: 0; right: 0;
    text-align: center;
  }
  .contact__name {
    color: var(--navy); font-weight: 600; font-size: 16px; letter-spacing: -0.2px;
    line-height: 1.2;
  }
  .contact__phones {
    margin-top: 4px; font-size: 11px; color: var(--ink-soft); line-height: 1.3;
  }
  .contact__label { color: var(--navy); font-weight: 700; }
  .contact__divider {
    display: inline-block; width: 1px; height: 12px; background: var(--navy);
    vertical-align: -2px; margin: 0 6px;
  }
  .contact__email {
    margin-top: 3px; font-size: 10.5px; color: var(--ink-soft); letter-spacing: 0.3px;
  }

  .card__rule {
    position: absolute; left: 0; right: 0; bottom: 20px; height: 2px; background: var(--rule);
  }
  .card__band {
    position: absolute; left: 0; right: 0; bottom: 0; height: 18px; background: var(--navy);
  }

  /* Back */
  .card--back {
    top: 415px; background: var(--navy);
    display: flex; justify-content: center; align-items: center; gap: 14px;
  }
  .card--back .brand__square { background: var(--white); width: 44px; height: 44px; }
  .card--back .brand__name { color: var(--white); }
  .card--back .brand__line1 { font-size: 15px; }
  .card--back .brand__line2 { font-size: 30px; }
</style>
</head>
<body>
<main class="canvas">
  <section class="card card--front" aria-label="Frente de la tarjeta">
    <div class="brand">
      <span class="brand__square"></span>
      <span class="brand__name">
        <span class="brand__line1">Desarrollos</span>
        <span class="brand__line2">Tolvani</span>
      </span>
    </div>
    <div class="contact">
      <p class="contact__name">Rodrigo Ulloa Benítez</p>
      <p class="contact__phones">
        <span class="contact__label">Cel :</span> (81) 82 19 57 46<span class="contact__divider"></span><span class="contact__label">Of :</span> (81) 86 72 13 95
      </p>
      <p class="contact__email">rulloab@correovelo.mx</p>
    </div>
    <div class="card__rule"></div>
    <div class="card__band"></div>
  </section>

  <section class="card card--back" aria-label="Reverso de la tarjeta">
    <span class="brand__square"></span>
    <span class="brand__name">
      <span class="brand__line1">Desarrollos</span>
      <span class="brand__line2">Tolvani</span>
    </span>
  </section>
</main>
</body>
</html>
```